We need a laundry sheet packingbox desgin

-look at our website plooimoes.nl to be in line with our house style/collor
We are a perfume seller and would like to offer also wasshingsheets with NO SMELL, so the customers can buy this incombination with our washingperfumes.
-the wassingheets will be neutrale(NO SMELL)
-it will be for the Dutch market
The next points should be on the desgin of the package
-our brand name: PLOOIMOES
-product name: WASSTRIPS
-(contains) Bevat: 30 wasstrips
-30 wasstrips = 60 wasbeurten
Please take some inspiration of others sellers & regarding eco friendly symbols etc.:
velunta.com & doxamp.nl
Backside information will be provided afther we found the right desgin
Please look at attachement pdf open box.
Here you can find the pdf design where you need to customize:
https://fy.qo/t-Lr8KxPq2Zh

```html
<!DOCTYPE html>
<html lang="nl">
<head>
<meta charset="utf-8">
<title>Plooimoes Wasstrips – verpakking voorzijde</title>
<link href="https://fonts.googleapis.com/css2?family=Playfair+Display:wght@400;900&family=Poppins:wght@400;600;700&display=swap" rel="stylesheet">
<style>
  :root{
    --stage:#3a3a3a;
    --box-black:#050505;
    --paper:#f2f1ee;
    --paper-shade:#e6e3dc;
    --gold:#c9a13f;
    --gold-light:#e2c063;
    --gold-deep:#a47a22;
  }
  *{margin:0;padding:0;box-sizing:border-box}
  html,body{width:900px;height:1200px;overflow:hidden;background:var(--stage)}
  .canvas{position:relative;width:900px;height:1200px;background:var(--stage)}
  .box-front{
    position:absolute;left:90px;top:60px;width:720px;height:1080px;
    background:var(--box-black);overflow:hidden;
  }
  .box-front__pattern{
    position:absolute;inset:0;
    background:radial-gradient(circle at 30% 65%, #15120b 0%, var(--box-black) 70%);
  }
  .box-front__shape{position:absolute;inset:0;width:720px;height:1080px}
  .brand{
    position:absolute;left:0;right:0;top:170px;
    display:flex;flex-direction:column;align-items:center;gap:26px;
    padding-left:90px;
  }
  .brand__mark{width:54px;height:54px;border-radius:50%;background:var(--gold)}
  .brand__name{
    font-family:"Playfair Display",serif;font-weight:400;font-size:34px;
    letter-spacing:1px;color:var(--gold-deep);
  }
  .specs{position:absolute;left:48px;top:440px;display:flex;gap:48px;align-items:center}
  .spec{display:flex;align-items:center;gap:10px;color:var(--gold)}
  .spec__icon{width:84px;height:64px}
  .spec__icon--machine{width:66px;height:66px}
  .spec__value{font-family:"Poppins",sans-serif;line-height:1}
  .spec__number{display:block;font-size:30px;font-weight:600}
  .spec__label{display:block;font-size:15px;font-weight:400}
  .product-name{
    position:absolute;left:40px;top:560px;
    font-family:"Playfair Display",serif;font-weight:900;font-size:132px;line-height:1;
    color:var(--gold);
    background:linear-gradient(90deg,var(--gold-deep),var(--gold-light) 60%,var(--gold));
    -webkit-background-clip:text;background-clip:text;-webkit-text-fill-color:transparent;
  }
  .claims{
    position:absolute;left:50px;top:770px;list-style:none;
    font-family:"Poppins",sans-serif;font-size:24px;line-height:1.3;color:var(--gold);
  }
  .claims strong{font-weight:700}
  .usage-illustration{
    position:absolute;left:60px;top:900px;width:600px;height:150px;border-radius:6px;
    background:linear-gradient(90deg,#5a4316,#b68a32 50%,#5a4316);opacity:.55;
  }
</style>
</head>
<body>
<main class="canvas">
  <section class="box-front">
    <div class="box-front__pattern" role="img" aria-label="Fijn goudkleurig bladerenpatroon op zwarte achtergrond"></div>

    <svg class="box-front__shape" viewBox="0 0 720 1080" aria-hidden="true">
      <defs>
        <linearGradient id="goldBand" x1="0" y1="0" x2="1" y2="1">
          <stop offset="0" stop-color="#a47a22"/>
          <stop offset=".5" stop-color="#e2c063"/>
          <stop offset="1" stop-color="#c9a13f"/>
        </linearGradient>
      </defs>
      <path d="M0,0 H720 V720 C690,560 610,430 470,395 C300,352 110,300 0,0 Z" fill="url(#goldBand)"/>
      <path d="M0,0 H720 V650 C680,520 600,410 460,375 C300,335 100,280 0,-10 Z" fill="#f2f1ee"/>
    </svg>

    <header class="brand">
      <span class="brand__mark" aria-hidden="true"></span>
      <span class="brand__name">PLOOIMOES</span>
    </header>

    <div class="specs">
      <div class="spec">
        <svg class="spec__icon" viewBox="0 0 84 64" aria-hidden="true">
          <path d="M30,4 H80 L54,58 H4 Z" fill="#c9a13f"/>
          <path d="M34,10 H84 L58,64 H8" fill="none" stroke="#c9a13f" stroke-width="3"/>
        </svg>
        <span class="spec__value"><span class="spec__number">30</span><span class="spec__label">wasstrip</span></span>
      </div>
      <div class="spec">
        <svg class="spec__icon spec__icon--machine" viewBox="0 0 66 66" aria-hidden="true">
          <rect x="2" y="2" width="62" height="62" rx="5" fill="none" stroke="#c9a13f" stroke-width="3"/>
          <rect x="8" y="8" width="50" height="50" rx="3" fill="#c9a13f"/>
          <circle cx="33" cy="33" r="15" fill="#050505"/>
          <path d="M19,36 C26,30 40,30 47,36 A15,15 0 0 1 19,36 Z" fill="#f2f1ee"/>
        </svg>
        <span class="spec__value"><span class="spec__number">60</span><span class="spec__label">wasbeurten</span></span>
      </div>
    </div>

    <h1 class="product-name">Wasstrips</h1>

    <ul class="claims">
      <li><strong>100 wasbeurten</strong> per verpakking</li>
      <li>100% <strong>Milieuvriendelijk</strong></li>
      <li>Geschikt voor alle wasbehoeften</li>
    </ul>

    <div class="usage-illustration" role="img" aria-label="Gebruiksillustratie: vuil shirt plus wasstrip, wasmachine, schoon shirt"></div>
  </section>
</main>
</body>
</html>
```